Verra needs a new design we have an updated logo and want a high qualitative high end feel

feel and aesthetic should be high qualitative like the packaging in a zuvi or the qualatative weight/feel of an zuvi design. modern, elegant bold.probably just the verra logo on the backone vesion could be blue background white letter ... open to ideas
Target Market(s)
legal, insurance , medical, finance rho 740
Industry/Entity Type
Information Technology
Font styles to use
Serif

```html
<!DOCTYPE html>
<html lang="en">
<head>
<meta charset="utf-8">
<title>Verra Managed Services Group – Business Card</title>
<link href="https://fonts.googleapis.com/css2?family=Tinos:wght@400;700&display=swap" rel="stylesheet">
<style>
  :root {
    --navy: #1b2a3c;
    --navy-soft: #3f5673;
    --paper: #ffffff;
    --ink: #1a2433;
    --stage: #2b2b2d;
  }
  * { box-sizing: border-box; margin: 0; padding: 0; }
  html, body { width: 1200px; height: 900px; overflow: hidden; }
  body {
    background: var(--stage);
    font-family: "Tinos", "Times New Roman", serif;
    display: flex;
    flex-direction: column;
    align-items: center;
    justify-content: center;
    gap: 40px;
  }
  .card {
    width: 700px;
    height: 400px;
    position: relative;
    overflow: hidden;
  }
  .card--back {
    background: var(--navy);
    color: var(--paper);
  }
  .card--front {
    background: var(--paper);
    color: var(--ink);
  }
  .wordmark {
    font-family: "Tinos", "Times New Roman", serif;
    font-weight: 700;
    letter-spacing: 1px;
    line-height: 1;
  }
  .card--back .wordmark {
    position: absolute;
    left: 0; right: 0;
    top: 130px;
    text-align: center;
    font-size: 96px;
    color: var(--paper);
  }
  .card--back .website {
    position: absolute;
    left: 0; right: 0;
    bottom: 70px;
    text-align: center;
    font-size: 20px;
    letter-spacing: 1px;
  }
  .card--front .wordmark {
    position: absolute;
    left: 60px;
    top: 110px;
    font-size: 84px;
    color: var(--navy);
  }
  .contact {
    position: absolute;
    right: 50px;
    top: 150px;
    width: 300px;
  }
  .contact__name {
    font-size: 26px;
    font-weight: 700;
    color: var(--ink);
  }
  .contact__title {
    font-size: 20px;
    color: var(--navy-soft);
    margin: 4px 0 14px 14px;
  }
  .contact__list { list-style: none; }
  .contact__item {
    display: flex;
    align-items: center;
    gap: 10px;
    font-size: 18px;
    line-height: 26px;
    color: var(--ink);
  }
  .contact__item svg { width: 16px; height: 16px; flex: none; fill: var(--navy-soft); }
  .card__band {
    position: absolute;
    left: 0; right: 0; bottom: 0;
    height: 22px;
    background: var(--navy);
  }
</style>
</head>
<body>
  <section class="card card--back">
    <div class="wordmark">Verra</div>
    <div class="website">www.verramanagedservices.com</div>
  </section>

  <section class="card card--front">
    <div class="wordmark">Verra</div>
    <div class="contact">
      <div class="contact__name">Julian Whitmore</div>
      <div class="contact__title">CEO/Founder</div>
      <ul class="contact__list">
        <li class="contact__item">
          <svg viewBox="0 0 16 16"><path d="M3.6 1.5l2.3 2.6-1.3 1.7c.9 2 2.5 3.6 4.5 4.6l1.7-1.3 2.6 2.3-1.4 2.2C7.2 13.4 2.6 8.8 1.4 3z"/></svg>
          214-555-0187
        </li>
        <li class="contact__item">
          <svg viewBox="0 0 16 16"><path d="M3.6 1.5l2.3 2.6-1.3 1.7c.9 2 2.5 3.6 4.5 4.6l1.7-1.3 2.6 2.3-1.4 2.2C7.2 13.4 2.6 8.8 1.4 3z"/></svg>
          214-555-0187
        </li>
        <li class="contact__item">
          <svg viewBox="0 0 16 16"><path d="M1 3h14v10H1z M1.5 3.5L8 9l6.5-5.5" fill="none" stroke="#3f5673" stroke-width="1.4"/></svg>
          info@verramanagedservices.com
        </li>
        <li class="contact__item">
          <svg viewBox="0 0 16 16"><circle cx="8" cy="8" r="6.5" fill="none" stroke="#3f5673" stroke-width="1.3"/><path d="M1.5 8h13M8 1.5c-3 3.5-3 9.5 0 13M8 1.5c3 3.5 3 9.5 0 13" fill="none" stroke="#3f5673" stroke-width="1.1"/></svg>
          www.verramanagedservices.com
        </li>
      </ul>
    </div>
    <div class="card__band"></div>
  </section>
</body>
</html>
```